Lucia Verde a furniture, interior design and home decor Brand

I need complete stationary for a new brand, business card, postcard, letter head, shipping envelopes, tissue paper, etc... I would like to use copper foil on some of these items. I have a logo design. I would like to see

Furniture,Interior Design & Home Decor

Interior Design

Colors
606060
7f7f7f

Must have
• My signature style is spanish medeterrenean, my brand colors is charcoal gray with copper. Would love to see a wrought iron panel illustration created, I have attahced a few samples of wrought iron illustration I am attracted to, also an example of packing that has the pattern in foil.
Should not have
• Will not be using the word Design, only Lucia Verde and LV icon

```html
<!DOCTYPE html>
<html lang="en">
<head>
<meta charset="utf-8">
<title>Lucia Verde — Business Card</title>
<link rel="stylesheet" href="https://fonts.googleapis.com/css2?family=Jost:wght@400;500;700&display=swap">
<style>
  :root {
    --backdrop: #e6e6e6;
    --charcoal: #505050;
    --charcoal-text: #606060;
    --copper: #d9682f;
    --copper-light: #f2a678;
    --copper-deep: #c9561f;
    --paper: #ffffff;
  }
  * { margin: 0; padding: 0; box-sizing: border-box; }
  html, body {
    width: 1200px; height: 1108px; overflow: hidden;
    background: var(--backdrop);
    font-family: "Jost", sans-serif;
  }
  .card {
    position: absolute; left: 160px;
    width: 880px; height: 500px;
    border-radius: 28px;
    overflow: hidden;
    box-shadow: 0 6px 18px rgba(0,0,0,0.18);
  }
  /* Front */
  .card-front { top: 36px; background: var(--charcoal); }
  .front-circle {
    position: absolute; left: 120px; top: 40px;
    width: 360px; height: 360px;
    border: 4px solid var(--copper);
    border-radius: 50%;
  }
  .front-wordmark {
    position: absolute; right: 80px; bottom: 56px;
    color: var(--copper);
    font-size: 56px; font-weight: 400; letter-spacing: 1px;
    white-space: nowrap;
  }
  /* Back */
  .card-back { top: 572px; background: var(--paper); }
  .name-band {
    position: absolute; left: 0; top: 40px;
    width: 530px; height: 120px;
    background: linear-gradient(90deg, var(--copper-deep) 0%, var(--copper-light) 45%, var(--copper) 100%);
    padding: 22px 0 0 70px;
    color: var(--paper);
  }
  .name-band .person { font-size: 38px; font-weight: 700; line-height: 1.1; }
  .name-band .role { font-size: 22px; font-weight: 500; }
  .back-brand {
    position: absolute; left: 500px; top: 60px;
    display: flex; align-items: center; gap: 16px;
    z-index: 1;
  }
  .back-brand .mark-circle {
    width: 92px; height: 92px;
    border: 2px solid var(--copper);
    border-radius: 50%;
    background: var(--paper);
    flex: none;
  }
  .back-brand .wordmark {
    color: var(--copper);
    font-size: 34px; font-weight: 400; white-space: nowrap;
  }
  .contact-list {
    position: absolute; left: 60px; top: 290px;
    list-style: none;
    color: var(--charcoal-text);
    font-size: 24px; line-height: 1.5;
  }
  .contact-list li { display: flex; align-items: center; gap: 14px; }
  .contact-list svg { width: 20px; height: 20px; flex: none; }
  .address {
    position: absolute; right: 60px; bottom: 50px;
    text-align: right;
    font-style: normal;
    color: var(--charcoal-text);
    font-size: 26px; line-height: 1.35;
  }
</style>
</head>
<body>
  <section class="card card-front">
    <div class="front-circle"></div>
    <div class="front-wordmark">Lucia Verde</div>
  </section>

  <section class="card card-back">
    <div class="name-band">
      <div class="person">Lucia Verde</div>
      <div class="role">CEO/Founder</div>
    </div>
    <div class="back-brand">
      <div class="mark-circle"></div>
      <div class="wordmark">Lucia Verde</div>
    </div>

    <ul class="contact-list">
      <li>
        <svg viewBox="0 0 20 20" aria-hidden="true"><path fill="#d9682f" d="M5 2l3 4-2 2c1 2 3 4 5 5l2-2 4 3-2 3C9 17 3 11 2 5z"/></svg>
        541 220 7193
      </li>
      <li>
        <svg viewBox="0 0 20 20" aria-hidden="true"><rect x="5" y="2" width="10" height="16" rx="2" fill="none" stroke="#d9682f" stroke-width="2"/><circle cx="10" cy="15" r="1" fill="#d9682f"/></svg>
        541 380 4426
      </li>
      <li>
        <svg viewBox="0 0 20 20" aria-hidden="true"><rect x="2" y="4" width="16" height="12" fill="#d9682f"/><path d="M2 4l8 7 8-7" fill="none" stroke="#fff" stroke-width="1.5"/></svg>
        hello@luciaverde.com
      </li>
    </ul>

    <address class="address">
      2140 Cedar Hollow Road<br>
      Bend, Oregon 97701<br>
      www.luciaverde.com
    </address>
  </section>
</body>
</html>
```